Need restaurant menu selection app design

you walk into a restaurant for the first time and wonder what you should eat.
You grab your phone. launch the app. It knows your current location and the name of the restaurant you're in.
You press a button and the app recommends what you should eat from the restaurant's menu. Based on your food preferences (you set when you first download the app) or based on similar foods they previously ate elsewhere and liked.
What I need are a few screen design for the following flow steps:
1. Home screen when you pull up the app - it should identify the location and name of the restaurant and a call to action to see what they should eat
2. A list of what you might like in 2 groups: based on your profile & based on what you previously ate and liked. Each list item will feature the name of the menu item, ingredients, calorie count
3. Detail page for a menu selection with a photo, details above, other people's ratings. a button to say yes I will eat this and a button for Next and the page will be replaced with the next item on the list.
That's it: 3 screens at least.
Just uploaded a wireframe in pdf to provide some directional context.
Restaurant

```html
<!DOCTYPE html>
<html lang="en">
<head>
<meta charset="utf-8">
<title>NOSH – restaurant menu app screens</title>
<link rel="stylesheet" href="https://fonts.googleapis.com/css2?family=Arimo:wght@400;700&display=swap">
<style>
  :root {
    --page: #ffffff;
    --status: #0d0d0d;
    --green-top: #a9cf74;
    --green-mid: #86b94a;
    --green-dark: #5e8f1f;
    --green-text: #79ad2c;
    --tan-light: #e7c68f;
    --tan: #d9a95c;
    --brown: #b9772a;
    --orange: #e88a1a;
    --star-off: #d8cfbf;
    --content-bg: #eef6df;
    --content-bg-2: #dcecc2;
    --divider: #c9a46a;
    --map-base: #e8e4dc;
    --map-park: #cfe0b5;
    --photo-a: #d9c39a;
    --photo-b: #8a6a3e;
    --white: #ffffff;
  }
  * { box-sizing: border-box; margin: 0; padding: 0; }
  html, body { width: 1200px; height: 1000px; overflow: hidden; background: var(--page); }
  body { font-family: "Arimo", Arial, sans-serif; position: relative; }

  .screens { position: absolute; left: 70px; top: 260px; display: flex; gap: 50px; }
  .screen {
    width: 320px; height: 480px; display: flex; flex-direction: column;
    overflow: hidden; background: var(--content-bg);
    box-shadow: 0 2px 10px rgba(0,0,0,.18);
  }

  /* status bar */
  .status-bar {
    height: 20px; background: var(--status); color: var(--white);
    display: flex; align-items: center; justify-content: space-between;
    padding: 0 8px; font-size: 12px; font-weight: 700; position: relative;
  }
  .status-bar .carrier { display: flex; align-items: center; gap: 4px; }
  .status-bar .time { position: absolute; left: 0; right: 0; text-align: center; font-size: 14px; }
  .battery { width: 22px; height: 10px; border: 1.5px solid #ccc; border-radius: 2px; padding: 1px; }
  .battery span { display: block; height: 100%; background: #ddd; }

  /* header */
  .app-header {
    height: 36px; display: flex; align-items: center; gap: 6px; padding: 0 6px;
    background: linear-gradient(var(--green-top), var(--green-mid));
  }
  .search-field {
    flex: 1; height: 26px; border-radius: 13px; background: var(--white);
    display: flex; align-items: center; padding: 0 4px 0 8px; gap: 6px;
    box-shadow: inset 0 1px 3px rgba(0,0,0,.35);
  }
  .search-field .query { flex: 1; color: #888; font-size: 13px; border-left: 1px solid #ccc; padding-left: 6px; }
  .book-btn { width: 28px; height: 18px; border-radius: 9px; background: var(--orange); display: flex; align-items: center; justify-content: center; }

  /* tabs */
  .tabs { height: 26px; display: flex; }
  .tab {
    flex: 1; display: flex; align-items: center; justify-content: center;
    color: var(--white); font-size: 13px;
    background: linear-gradient(var(--tan-light), var(--tan));
  }
  .tab.is-active { background: linear-gradient(#cf8f3c, var(--brown)); box-shadow: inset 0 0 4px rgba(0,0,0,.3); }

  .content { flex: 1; position: relative; overflow: hidden; background: linear-gradient(160deg, var(--content-bg), var(--content-bg-2)); }

  /* bottom nav */
  .bottom-nav {
    height: 44px; display: flex;
    background: linear-gradient(var(--green-mid), var(--green-dark));
  }
  .nav-item {
    flex: 1; display: flex; flex-direction: column; align-items: center; justify-content: center;
    gap: 2px; color: var(--white); font-size: 11px;
  }
  .nav-item.is-active { background: rgba(255,255,255,.22); font-weight: 700; margin: 0 20px; }

  /* map */
  .map { position: absolute; inset: 0; background:
      linear-gradient(125deg, transparent 60%, var(--map-park) 60%), var(--map-base); }

  /* menu list */
  .menu-list { list-style: none; }
  .menu-item {
    height: 58px; display: flex; align-items: center; padding: 0 10px 0 16px;
    border-bottom: 1px solid var(--divider);
  }
  .menu-item .info { flex: 1; }
  .menu-item .name { color: var(--green-text); font-size: 15px; }
  .menu-item .ingredients { color: var(--orange); font-size: 7.5px; font-weight: 700; margin-top: 6px; }
  .menu-item .meta { width: 50px; text-align: right; margin-right: 12px; }
  .stars { color: var(--orange); font-size: 8px; letter-spacing: 0; }
  .stars .off { color: var(--star-off); }
  .price { color: var(--orange); font-size: 10px; font-weight: 700; margin-top: 6px; }

  /* recommendation detail */
  .detail { padding: 10px 0 0; text-align: center; }
  .restaurant-name { color: var(--orange); font-size: 15px; font-weight: 400; padding-bottom: 8px; border-bottom: 1px solid #d5e6bd; margin: 0 6px; }
  .tagline { color: var(--green-text); font-size: 10px; margin-top: 10px; }
  .detail .stars { text-align: right; padding-right: 30px; margin-top: 2px; }
  .carousel { display: flex; align-items: center; justify-content: center; gap: 8px; margin-top: 2px; }
  .dish-photo { width: 244px; height: 166px; border: 3px solid var(--white); box-shadow: 0 1px 3px rgba(0,0,0,.3);
    background: radial-gradient(circle at 50% 55%, var(--photo-a), var(--photo-b)); }
  .dish-caption { text-align: left; padding: 6px 38px 0; }
  .dish-caption .name { color: var(--green-text); font-size: 11px; }
  .dish-caption .row { display: flex; justify-content: space-between; margin-top: 3px; }
  .dish-caption .ingredients { color: var(--orange); font-size: 6.5px; font-weight: 700; }
  .more-info { color: var(--green-dark); font-size: 7px; font-weight: 700; }
  .actions { display: flex; justify-content: space-around; margin-top: 28px; }
  .action { display: flex; flex-direction: column; align-items: center; gap: 4px; color: var(--orange); font-size: 7px; }
  .action .glyph { height: 16px; display: flex; align-items: center; }
</style>
</head>
<body>
<main class="screens">

  <!-- Screen: location -->
  <section class="screen">
    <div class="status-bar">
      <span class="carrier"><svg width="14" height="9"><rect x="0" y="6" width="2" height="3" fill="#fff"/><rect x="3" y="4" width="2" height="5" fill="#fff"/><rect x="6" y="2" width="2" height="7" fill="#fff"/><rect x="9" y="0" width="2" height="9" fill="#fff"/></svg>Carrier</span>
      <span class="time">6:40 PM</span>
      <span class="battery"><span></span></span>
    </div>
    <header class="app-header">
      <svg width="10" height="14" viewBox="0 0 10 14"><path d="M5 0a5 5 0 0 1 5 5c0 4-5 9-5 9S0 9 0 5a5 5 0 0 1 5-5z" fill="#fff"/></svg>
      <div class="search-field">
        <svg width="14" height="14" viewBox="0 0 14 14"><circle cx="6" cy="6" r="4.5" stroke="#555" stroke-width="2" fill="none"/><line x1="9.5" y1="9.5" x2="13" y2="13" stroke="#555" stroke-width="2.2"/></svg>
        <span class="query">NOSH</span>
        <span class="book-btn"><svg width="16" height="11" viewBox="0 0 16 11"><path d="M1 1h5a2 2 0 0 1 2 2v7a2 2 0 0 0-2-1H1zM15 1h-5a2 2 0 0 0-2 2v7a2 2 0 0 1 2-1h5z" stroke="#fff" stroke-width="1.4" fill="none"/></svg></span>
      </div>
    </header>
    <nav class="tabs"><span class="tab">Location</span><span class="tab is-active">Menu</span></nav>
    <div class="content">
      <div class="map" role="img" aria-label="Street map showing the current restaurant's location with a pin and info bubble"></div>
    </div>
    <nav class="bottom-nav">
      <span class="nav-item is-active"><svg width="14" height="16" viewBox="0 0 14 16"><path d="M3 9a3 3 0 0 1 1-6 3.5 3.5 0 0 1 6 0 3 3 0 0 1 1 6v5H3z" fill="#fff"/></svg>My Location</span>
      <span class="nav-item"><svg width="16" height="16" viewBox="0 0 24 24"><path d="M12 1l3.4 7 7.6 1-5.5 5.3 1.3 7.7L12 18.4 5.2 22l1.3-7.7L1 9l7.6-1z" fill="#fff"/></svg>My Favoris</span>
      <span class="nav-item"><svg width="18" height="16" viewBox="0 0 24 21"><path d="M12 21S0 13 0 6a6 6 0 0 1 12-1 6 6 0 0 1 12 1c0 7-12 15-12 15z" fill="#fff"/></svg>you'll like</span>
    </nav>
  </section>

  <!-- Screen: menu list -->
  <section class="screen">
    <div class="status-bar">
      <span class="carrier"><svg width="14" height="9"><rect x="0" y="6" width="2" height="3" fill="#fff"/><rect x="3" y="4" width="2" height="5" fill="#fff"/><rect x="6" y="2" width="2" height="7" fill="#fff"/><rect x="9" y="0" width="2" height="9" fill="#fff"/></svg>Carrier</span>
      <span class="time">6:40 PM</span>
      <span class="battery"><span></span></span>
    </div>
    <header class="app-header">
      <svg width="10" height="14" viewBox="0 0 10 14"><path d="M5 0a5 5 0 0 1 5 5c0 4-5 9-5 9S0 9 0 5a5 5 0 0 1 5-5z" fill="#fff"/></svg>
      <div class="search-field">
        <svg width="14" height="14" viewBox="0 0 14 14"><circle cx="6" cy="6" r="4.5" stroke="#555" stroke-width="2" fill="none"/><line x1="9.5" y1="9.5" x2="13" y2="13" stroke="#555" stroke-width="2.2"/></svg>
        <span class="query">NOSH</span>
        <span class="book-btn"><svg width="16" height="11" viewBox="0 0 16 11"><path d="M1 1h5a2 2 0 0 1 2 2v7a2 2 0 0 0-2-1H1zM15 1h-5a2 2 0 0 0-2 2v7a2 2 0 0 1 2-1h5z" stroke="#fff" stroke-width="1.4" fill="none"/></svg></span>
      </div>
    </header>
    <nav class="tabs"><span class="tab is-active">Location</span><span class="tab">Menu</span></nav>
    <div class="content">
      <ul class="menu-list">
        <li class="menu-item"><div class="info"><div class="name">Linguini ai Frutti di Mare</div><div class="ingredients">Ingredients: alade de la Mer (shrimps, mussels, shells...</div></div><div class="meta"><div class="stars">★★★★★</div><div class="price">$$</div></div><svg width="8" height="14" viewBox="0 0 8 14"><path d="M1 1l6 6-6 6" stroke="#b9772a" stroke-width="2" fill="none"/></svg></li>
        <li class="menu-item"><div class="info"><div class="name">Spaghetti alle Vongole</div><div class="ingredients">Ingredients: alade de la Mer (shrimps, mussels, shells...</div></div><div class="meta"><div class="stars">★★★<span class="off">★★</span></div><div class="price">$</div></div><svg width="8" height="14" viewBox="0 0 8 14"><path d="M1 1l6 6-6 6" stroke="#b9772a" stroke-width="2" fill="none"/></svg></li>
        <li class="menu-item"><div class="info"><div class="name">Raviolini ai Carciofi</div><div class="ingredients">Ingredients: alade de la Mer (shrimps, mussels, shells...</div></div><div class="meta"><div class="stars">★★★★★</div><div class="price">$$$</div></div><svg width="8" height="14" viewBox="0 0 8 14"><path d="M1 1l6 6-6 6" stroke="#b9772a" stroke-width="2" fill="none"/></svg></li>
        <li class="menu-item"><div class="info"><div class="name">Scaloppa alla Milanese</div><div class="ingredients">Ingredients: alade de la Mer (shrimps, mussels, shells...</div></div><div class="meta"><div class="stars">★★★★<span class="off">★</span></div><div class="price">$</div></div><svg width="8" height="14" viewBox="0 0 8 14"><path d="M1 1l6 6-6 6" stroke="#b9772a" stroke-width="2" fill="none"/></svg></li>
        <li class="menu-item"><div class="info"><div class="name">Insalata ai Carciofi</div><div class="ingredients">Ingredients: alade de la Mer (shrimps, mussels, shells...</div></div><div class="meta"><div class="stars">★★★<span class="off">★★</span></div><div class="price">$$</div></div><svg width="8" height="14" viewBox="0 0 8 14"><path d="M1 1l6 6-6 6" stroke="#b9772a" stroke-width="2" fill="none"/></svg></li>
        <li class="menu-item"><div class="info"><div class="name">Gnocchi ai Fungh</div><div class="ingredients">Ingredients: alade de la Mer (shrimps, mussels, shells...</div></div><div class="meta"><div class="stars">★★★★<span class="off">★</span></div><div class="price">$$</div></div><svg width="8" height="14" viewBox="0 0 8 14"><path d="M1 1l6 6-6 6" stroke="#b9772a" stroke-width="2" fill="none"/></svg></li>
      </ul>
    </div>
    <nav class="bottom-nav">
      <span class="nav-item"><svg width="14" height="16" viewBox="0 0 14 16"><path d="M3 9a3 3 0 0 1 1-6 3.5 3.5 0 0 1 6 0 3 3 0 0 1 1 6v5H3z" fill="#fff"/></svg>My Location</span>
      <span class="nav-item"><svg width="16" height="16" viewBox="0 0 24 24"><path d="M12 1l3.4 7 7.6 1-5.5 5.3 1.3 7.7L12 18.4 5.2 22l1.3-7.7L1 9l7.6-1z" fill="#fff"/></svg>My Favoris</span>
      <span class="nav-item"><svg width="18" height="16" viewBox="0 0 24 21"><path d="M12 21S0 13 0 6a6 6 0 0 1 12-1 6 6 0 0 1 12 1c0 7-12 15-12 15z" fill="#fff"/></svg>you'll like</span>
    </nav>
  </section>

  <!-- Screen: recommendation detail -->
  <section class="screen">
    <div class="status-bar">
      <span class="carrier"><svg width="14" height="9"><rect x="0" y="6" width="2" height="3" fill="#fff"/><rect x="3" y="4" width="2" height="5" fill="#fff"/><rect x="6" y="2" width="2" height="7" fill="#fff"/><rect x="9" y="0" width="2" height="9" fill="#fff"/></svg>Carrier</span>
      <span class="time">6:40 PM</span>
      <span class="battery"><span></span></span>
    </div>
    <header class="app-header">
      <svg width="10" height="14" viewBox="0 0 10 14"><path d="M5 0a5 5 0 0 1 5 5c0 4-5 9-5 9S0 9 0 5a5 5 0 0 1 5-5z" fill="#fff"/></svg>
      <div class="search-field">
        <svg width="14" height="14" viewBox="0 0 14 14"><circle cx="6" cy="6" r="4.5" stroke="#555" stroke-width="2" fill="none"/><line x1="9.5" y1="9.5" x2="13" y2="13" stroke="#555" stroke-width="2.2"/></svg>
        <span class="query">NOSH</span>
        <span class="book-btn"><svg width="16" height="11" viewBox="0 0 16 11"><path d="M1 1h5a2 2 0 0 1 2 2v7a2 2 0 0 0-2-1H1zM15 1h-5a2 2 0 0 0-2 2v7a2 2 0 0 1 2-1h5z" stroke="#fff" stroke-width="1.4" fill="none"/></svg></span>
      </div>
    </header>
    <nav class="tabs"><span class="tab is-active">Location</span><span class="tab">Menu</span></nav>
    <div class="content detail">
      <h2 class="restaurant-name">Trattoria Bellavista</h2>
      <p class="tagline">Based on your tastes, you'll like</p>
      <div class="stars">★★★★★</div>
      <div class="carousel">
        <svg width="8" height="14" viewBox="0 0 8 14"><path d="M7 1L1 7l6 6" stroke="#e88a1a" stroke-width="2" fill="none"/></svg>
        <div class="dish-photo" role="img" aria-label="Photo of a plate of linguine with clams and mussels"></div>
        <svg width="8" height="14" viewBox="0 0 8 14"><path d="M1 1l6 6-6 6" stroke="#e88a1a" stroke-width="2" fill="none"/></svg>
      </div>
      <div class="dish-caption">
        <div class="name">Linguini ai Frutti di Mare</div>
        <div class="row"><span class="ingredients">Ingredients: alade de la Mer (shrimps, mussels, shells...</span><span class="more-info">More Info</span></div>
      </div>
      <div class="actions">
        <span class="action"><span class="glyph stars">★★★★★</span>Rate</span>
        <span class="action"><span class="glyph"><svg width="16" height="16" viewBox="0 0 24 24"><path d="M12 1l3.4 7 7.6 1-5.5 5.3 1.3 7.7L12 18.4 5.2 22l1.3-7.7L1 9l7.6-1z" fill="#e88a1a"/></svg></span>Add to favoris</span>
        <span class="action"><span class="glyph"><svg width="12" height="12" viewBox="0 0 12 12"><path d="M1 1l10 10M11 1L1 11" stroke="#e88a1a" stroke-width="2"/></svg></span>Dismiss</span>
      </div>
    </div>
    <nav class="bottom-nav">
      <span class="nav-item"><svg width="14" height="16" viewBox="0 0 14 16"><path d="M3 9a3 3 0 0 1 1-6 3.5 3.5 0 0 1 6 0 3 3 0 0 1 1 6v5H3z" fill="#fff"/></svg>My Location</span>
      <span class="nav-item"><svg width="16" height="16" viewBox="0 0 24 24"><path d="M12 1l3.4 7 7.6 1-5.5 5.3 1.3 7.7L12 18.4 5.2 22l1.3-7.7L1 9l7.6-1z" fill="#fff"/></svg>My Favoris</span>
      <span class="nav-item is-active"><svg width="18" height="16" viewBox="0 0 24 21"><path d="M12 21S0 13 0 6a6 6 0 0 1 12-1 6 6 0 0 1 12 1c0 7-12 15-12 15z" fill="#fff"/></svg>you'll like</span>
    </nav>
  </section>

</main>
</body>
</html>
```